Extremely Professional Lawyer needs letterhead for new boutique real estate law firm

I need letterhead for my new solo practice law firm. I practiced as a partner in a huge global law firm for years. Now I am starting a solo firm where I will deliver very high-quality legal services that are real-estate focused. The idea is that my practice will be very focused but that the services will be at the quality level provided by partners at high-profile law firms. The name of my law firm will be Brenn Law Group, LLC. For now, I am the only lawyer. I expect to negotiate and draft house sale/purchase contracts and close house deals. Eventually, I would like to do small-scale development deals for developer clients, a specialty of mine.

Industry/Entity Type

Boutique

```html
<!DOCTYPE html>
<html lang="en">
<head>
<meta charset="utf-8">
<title>Brenn Law Group, LLC – Letterhead</title>
<link rel="stylesheet" href="https://fonts.googleapis.com/css2?family=Cinzel:wght@600&family=Arimo:wght@700&display=swap">
<style>
  :root {
    --backdrop: #eef0f2;
    --paper: #ffffff;
    --brand-blue: #1496c4;
    --brand-blue-deep: #0d7fa6;
    --brand-blue-light: #7fd0ef;
    --accent-bright: #10aee6;
    --mist-grey: #dfe3e6;
    --ink-light: #ffffff;
  }
  * { margin: 0; padding: 0; box-sizing: border-box; }
  html, body { width: 900px; height: 1200px; overflow: hidden; }
  body {
    background: var(--backdrop);
    display: flex;
    align-items: center;
    justify-content: center;
  }
  .letterhead {
    position: relative;
    width: 640px;
    height: 905px;
    background: var(--paper);
    box-shadow: 0 6px 24px rgba(0,0,0,0.18);
    overflow: hidden;
  }
  .letterhead__art {
    position: absolute;
    inset: 0;
    width: 100%;
    height: 100%;
  }
  .firm-name {
    position: absolute;
    top: 28px;
    right: 20px;
    font-family: "Cinzel", "Trajan Pro", serif;
    font-weight: 600;
    font-size: 34px;
    letter-spacing: 0.3px;
    color: var(--ink-light);
    white-space: nowrap;
  }
  .company-details {
    position: absolute;
    left: 16px;
    top: 744px;
    font-family: "Arimo", Arial, sans-serif;
    font-weight: 700;
    font-size: 16px;
    line-height: 20px;
    color: var(--ink-light);
    list-style: none;
    white-space: nowrap;
  }
  .company-details__registry span + span { margin-left: 22px; }
</style>
</head>
<body>
  <main class="letterhead">
    <svg class="letterhead__art" viewBox="0 0 640 905" aria-hidden="true">
      <defs>
        <linearGradient id="header-band" x1="0" y1="0" x2="1" y2="0">
          <stop offset="0" stop-color="var(--brand-blue-deep)"/>
          <stop offset="0.5" stop-color="var(--brand-blue-light)"/>
          <stop offset="1" stop-color="var(--brand-blue)"/>
        </linearGradient>
        <linearGradient id="corner-wedge" x1="0" y1="0" x2="1" y2="0">
          <stop offset="0" stop-color="var(--brand-blue)"/>
          <stop offset="1" stop-color="var(--brand-blue-light)"/>
        </linearGradient>
        <radialGradient id="footer-band" cx="0.55" cy="0.3" r="0.65">
          <stop offset="0" stop-color="var(--accent-bright)"/>
          <stop offset="1" stop-color="var(--brand-blue-deep)"/>
        </radialGradient>
        <linearGradient id="footer-mist" x1="0" y1="0" x2="1" y2="0">
          <stop offset="0" stop-color="#ffffff"/>
          <stop offset="1" stop-color="var(--mist-grey)"/>
        </linearGradient>
      </defs>

      <!-- header -->
      <path class="header-shadow" d="M190,96 C380,120 520,114 640,100 V120 C480,132 320,128 190,96 Z" fill="var(--mist-grey)"/>
      <path class="header-band" d="M0,0 H640 V96 C420,112 200,96 0,20 Z" fill="url(#header-band)"/>
      <path class="header-highlight" d="M80,76 C240,96 430,98 610,84 C430,92 240,92 80,76 Z" fill="#ffffff" opacity="0.6"/>
      <path class="corner-wedge" d="M0,20 C80,52 150,78 215,88 C120,88 45,104 0,125 Z" fill="url(#corner-wedge)"/>

      <!-- footer -->
      <path class="footer-mist" d="M0,735 C230,700 470,710 640,752 V905 H0 Z" fill="url(#footer-mist)"/>
      <path class="footer-band" d="M0,728 C210,700 440,720 640,822 V905 H0 Z" fill="url(#footer-band)"/>
    </svg>

    <h1 class="firm-name">Brenn Law Group, LLC</h1>

    <ul class="company-details">
      <li>Brenn Law Group, LLC</li>
      <li>14 Marlow Row, Hartfield, London, England, W9 3QA</li>
      <li>02079460321</li>
      <li>07700900418</li>
      <li>info@brennlawgroup.co.uk</li>
      <li>www.brennlawgroup.co.uk</li>
      <li class="company-details__registry"><span>Company No. 01234567</span><span>VAT No. GB 123456789</span></li>
    </ul>
  </main>
</body>
</html>
```